Falverino’s Artisan Pizzeria Menu Contest

I’m looking for a menu design for a new pizzeria - it’s farm to table type of restaurant - more upscale than a typical pizzeria - white washed wood interior with some industrial accents - I am looking for a creative menu layout using the attached sample menu items -
Falverino’s is an artisanal pizzeria with an atmosphere that will make you feel at home for any situation, first date, anniversary, business lunch, boys night out or girls night out with a menu inspired by the idea of a simple honest cooking paired with fresh – quality ingredients. Full service dining experience that is still casual but dedicated to extraordinary hospitality.
While developing the menu we have created a network of amazing farms and purveyors to supply our restaurant with fresh milled 100% California flour for our hand crafted dough, as well as sustainably farmed organic produce, meats and cheeses.
The menu includes classics like the Margherita pizza to daily seasonal specials, fresh salads to rustic small plates including moms meatball recipe to a fresh local burrata with handmade bread. Each dish reflects our passion for sourcing the freshest quality local ingredients.
To compliment the menu, Falverino’s serves an extensive wine list with selections focusing on Italian varietals. The cocktail program has been carefully crafted to offer something to entice ever palate and the beer list has unique selections of the world’s finest brewers.
Target Market(s)
25-45 year old men and women
Industry/Entity Type
American Restaurant
Requirements
Must have
- professional tone
Nice to have
- a balance of elegance and industrial (rustic)
Should not have
- photos or playful graphics etc..

```html
<!DOCTYPE html>
<html lang="en">
<head>
<meta charset="utf-8">
<title>Falverino’s Artisan Pizzeria Menu</title>
<link rel="stylesheet" href="https://fonts.googleapis.com/css2?family=Roboto+Slab:wght@500;700&family=Roboto+Condensed:wght@400&display=swap">
<style>
  :root {
    --ink: #1d1d1d;
    --paper: #ffffff;
    --backdrop: #ececec;
    --rule: #222222;
    --faint: #d8d8d8;
  }
  * { box-sizing: border-box; margin: 0; padding: 0; }
  html, body { width: 801px; height: 1200px; overflow: hidden; background: var(--backdrop); }
  .menu-sheet {
    position: absolute; left: 40px; top: 0;
    width: 1218px; height: 2030px;
    background: var(--paper);
    transform: scale(0.5911); transform-origin: 0 0;
    color: var(--ink);
    font-family: "Roboto Slab", serif;
  }
  .frame { position: absolute; left: 48px; top: 118px; width: 1128px; height: 1866px; border: 2px solid var(--rule); }
  .frame::after { content: ""; position: absolute; inset: 6px; border: 1.5px solid var(--rule); }
  .brand {
    position: absolute; left: 455px; top: 70px; width: 310px; height: 100px;
    background: var(--paper); z-index: 2;
    display: flex; align-items: center; justify-content: center;
    font-size: 56px; font-weight: 700; letter-spacing: 1px;
  }
  .rule { position: absolute; left: 117px; width: 990px; height: 3px; background: var(--rule); }
  .rule::before, .rule::after {
    content: ""; position: absolute; top: -3.5px; width: 10px; height: 10px; border-radius: 50%; background: var(--rule);
  }
  .rule::before { left: -5px; } .rule::after { right: -5px; }
  .section-title {
    position: absolute; left: 445px; width: 332px; height: 62px;
    background: var(--ink); color: var(--paper);
    font-size: 37px; font-weight: 700; letter-spacing: 5px;
    display: flex; align-items: center; justify-content: center;
  }
  .divider { position: absolute; left: 611px; width: 3px; background: var(--rule); }
  .item { position: absolute; width: 446px; }
  .col-l { left: 114px; } .col-r { left: 667px; }
  .item-name { font-size: 24px; font-weight: 700; line-height: 26px; letter-spacing: 0.3px; max-width: 350px; white-space: nowrap; }
  .item-name--long { font-size: 21px; letter-spacing: 0; }
  .item-desc { font-family: "Roboto Condensed", sans-serif; font-size: 14px; line-height: 18px; margin-top: 1px; white-space: nowrap; }
  .item-desc--small { font-size: 12px; line-height: 16px; }
  .price { position: absolute; top: 1px; right: 0; font-size: 20px; font-weight: 500; white-space: nowrap; }
  .soup-title { position: absolute; left: 114px; top: 866px; font-size: 37px; font-weight: 700; letter-spacing: 5px; }
  .soup-bar { position: absolute; left: 406px; top: 860px; width: 3px; height: 57px; background: var(--rule); }
  .soup-name { position: absolute; left: 428px; top: 878px; font-size: 22px; font-weight: 700; letter-spacing: 0.5px; }
  .soup-dash { position: absolute; left: 775px; top: 893px; width: 26px; height: 1px; background: var(--faint); }
  .soup-price { position: absolute; left: 822px; top: 880px; font-size: 20px; font-weight: 500; word-spacing: 10px; }
  .extras-band {
    position: absolute; left: 152px; top: 1712px; width: 922px; height: 59px; background: var(--ink); color: var(--paper);
    font-size: 37px; font-weight: 700; letter-spacing: 5px;
  }
  .extras-band span { position: absolute; top: 8px; }
  .extra { position: absolute; width: 418px; }
  .extra .item-name { max-width: none; }
  .extra .price { word-spacing: 12px; }
  .dip { width: 411px; }
  .inline-desc { font-family: "Roboto Condensed", sans-serif; font-size: 19px; font-weight: 400; margin-left: 10px; letter-spacing: 0; }
</style>
</head>
<body>
<main class="menu-sheet">
  <div class="frame"></div>
  <div class="brand">Falverino’s</div>

  <div class="rule" style="top:268px"></div>
  <h2 class="section-title" style="top:270px">APPETIZERS</h2>
  <div class="divider" style="top:352px;height:168px"></div>
  <div class="item col-l" style="top:352px"><div class="item-name">BRUSSELS</div><div class="item-desc">pan seared brussel sprouts with a drizzle of balsamic reduction<br>and parm and bread crumbs</div><span class="price">$ 10.00</span></div>
  <div class="item col-l" style="top:425px"><div class="item-name">MEATBALLS</div><div class="item-desc">moms meatballs handmade secret recipe for over 75 years</div><span class="price">$ 13.00</span></div>
  <div class="item col-l" style="top:483px"><div class="item-name">MUSSELS</div><div class="item-desc">New Zealand Mussels in a tomato broth</div><span class="price">$ 15.00</span></div>
  <div class="item col-r" style="top:352px"><div class="item-name">ROMANESCO</div><div class="item-desc">flash fried romanesco served atop a spicy aioli</div><span class="price">$ 11.00</span></div>
  <div class="item col-r" style="top:420px"><div class="item-name">CHICKEN WINGS</div><div class="item-desc">italian fried chicken wings with a kick</div><span class="price">$ 10.00</span></div>
  <div class="item col-r" style="top:481px"><div class="item-name">BURRATA</div><div class="item-desc">Local burrata served with apples grapes and fresh made bread</div><span class="price">$ 13.00</span></div>

  <div class="rule" style="top:543px"></div>
  <h2 class="section-title" style="top:545px">SALADS</h2>
  <div class="divider" style="top:645px;height:174px"></div>
  <div class="item col-l" style="top:643px"><div class="item-name">CHOPPED SALAD</div><div class="item-desc">Lettuce mix with tomato, onions, peppers, pepperoni,<br>chick peas, fresh mozz, italian herb ving</div><span class="price">$ 13.00</span></div>
  <div class="item col-l" style="top:720px"><div class="item-name">CAESAR SALAD</div><div class="item-desc">traditional caesar salad rich and creamy extra shaved parmesan</div><span class="price">$ 11.00</span></div>
  <div class="item col-l" style="top:780px"><div class="item-name">FARM SALAD</div><div class="item-desc">seasonal farmers market salad</div><span class="price">$ 15.00</span></div>
  <div class="item col-r" style="top:643px"><div class="item-name">GRILLED LITTLE GEM</div><div class="item-desc">Grilled little gems with bacon, tomato, red onions<br>and blue cheese dressing</div><span class="price">$ 11.00</span></div>
  <div class="item col-r" style="top:720px"><div class="item-name item-name--long">SPINACH AND ARUGULA SALAD</div><div class="item-desc">Spinach and argula, red pepperstossed in a lemon ving<br>and housemade croutons</div><span class="price">$ 12.00</span></div>

  <div class="rule" style="top:839px"></div>
  <h2 class="soup-title">DAILY SOUP</h2>
  <div class="soup-bar"></div>
  <div class="soup-name">EXAMPLE TOMATO BISQUE</div>
  <div class="soup-dash"></div>
  <div class="soup-price">$ 8.00</div>

  <div class="rule" style="top:936px"></div>
  <h2 class="section-title" style="top:938px">SANDWICHES</h2>
  <div class="divider" style="top:1045px;height:173px"></div>
  <div class="item col-l" style="top:1041px"><div class="item-name">ITALIAN SUB</div><div class="item-desc">Prociutto, salumi, turkey, provolone, lettuce, tomato<br>and herb aioli with spicy gardenia</div><span class="price">$ 13.00</span></div>
  <div class="item col-l" style="top:1118px"><div class="item-name">TURKEY SANDWICH</div><div class="item-desc">housemade bread - turkey, cheddar cheese,<br>butter lettuce, tomato and mustard aioli</div><span class="price">$ 12.00</span></div>
  <div class="item col-l" style="top:1180px"><div class="item-name">MEATBALL SUB</div><div class="item-desc">Moms meatballs melted provolone on a housemade roll</div><span class="price">$ 13.00</span></div>
  <div class="item col-r" style="top:1041px"><div class="item-name">VERDANT BURGER</div><div class="item-desc">Housemade bun - arugula , tomato, onion<br>and a sundried tomato spread</div><span class="price">$ 14.00</span></div>
  <div class="item col-r" style="top:1118px"><div class="item-name">CHICKEN SANDWICH</div><div class="item-desc">Fried chicken or chicken breast, provolone, argula,<br>tomato, served with a spicy aioli</div><span class="price">$ 13.00</span></div>

  <div class="rule" style="top:1249px"></div>
  <h2 class="section-title" style="top:1251px">PIZZAS</h2>
  <div class="divider" style="top:1365px;height:305px"></div>
  <div class="item col-l" style="top:1360px"><div class="item-name">MARGHERITA</div><div class="item-desc">Classic Margherita pizza - Fresh Mozz Tomato Sauce and Basil</div><span class="price">$ 14.00</span></div>
  <div class="item col-l" style="top:1422px"><div class="item-name">ORGANIC SAUSAGE</div><div class="item-desc">Organic Sausage Housemade Red Sauce Mozz hint of fennel</div><span class="price">$ 16.00</span></div>
  <div class="item col-l" style="top:1495px"><div class="item-name">PEPPERONI</div><div class="item-desc">Ashford Pepperoni - Housemade Red Sauce Chile flakes and Mozz</div><span class="price">$ 16.00</span></div>
  <div class="item col-l" style="top:1571px"><div class="item-name">SALUMI AND BURRATA</div><div class="item-desc">Salumi dried Red Sauce finished with whipped burrata</div><span class="price">$ 17.00</span></div>
  <div class="item col-l" style="top:1630px"><div class="item-name">DAILY SPECIAL</div><span class="price">$ 17.00</span></div>
  <div class="item col-r" style="top:1361px"><div class="item-name">MUSHROOM</div><div class="item-desc">Shaved mushrooms with a Parmesan cream and melted onions</div><span class="price">$ 15.00</span></div>
  <div class="item col-r" style="top:1421px"><div class="item-name">PROSCIUTTO AND EGG</div><div class="item-desc">Parma Prosciutto Parmesan cream with Valdberg<br>and gruyere finished with an organic egg</div><span class="price">$ 16.00</span></div>
  <div class="item col-r" style="top:1497px"><div class="item-name">QUARTTRO FORMAGGI</div><div class="item-desc item-desc--small">Four cheese combination - mozz - fontina - parm cream<br>and gruyere chile flakes and oregano</div><span class="price">$ 15.00</span></div>
  <div class="item col-r" style="top:1572px"><div class="item-name">FARMERS PIZZA</div><div class="item-desc">Seasonal vegatables cream sauce and a variety of cheese</div><span class="price">$ 17.00</span></div>
  <div class="item col-r" style="top:1630px"><div class="item-name">KETO FRIENDLY</div><div class="item-desc">Cauliflower crust, spinach and kale , parm cream sauce</div><span class="price">$ 17.00</span></div>

  <div class="rule" style="top:1710px"></div>
  <div class="extras-band"><span style="left:28px">CRUSTS</span><span style="left:514px">DIPS</span></div>
  <div class="divider" style="top:1800px;height:126px"></div>
  <div class="extra" style="left:152px;top:1796px"><div class="item-name">TRADITIONAL<span class="inline-desc">orginal crust you can't miss</span></div></div>
  <div class="extra" style="left:152px;top:1840px"><div class="item-name">GLUTEN FREE</div><div class="item-desc">best gluten friendly crust on the west coast</div><span class="price">$ 3.00</span></div>
  <div class="extra" style="left:152px;top:1891px"><div class="item-name">CAULIFLOWER</div><div class="item-desc">Vegans have needs</div><span class="price">$ 3.00</span></div>
  <div class="extra dip" style="left:666px;top:1795px"><div class="item-name">RANCH</div><span class="price">$ 1.00</span></div>
  <div class="extra dip" style="left:666px;top:1830px"><div class="item-name">TOMATO SAUCE</div><span class="price">$ 1.00</span></div>
  <div class="extra dip" style="left:666px;top:1867px"><div class="item-name">SPICY DIP</div><span class="price">$ 1.00</span></div>
  <div class="extra dip" style="left:666px;top:1906px"><div class="item-name">BLUE CHEESE</div><span class="price">$ 1.00</span></div>
</main>
</body>
</html>
```